Training Program Flyers

***Please note an update - the flyers should have somewhere a space that can include a special offer, which can be removed if not applicable with no impact to the design. Have uploaded a graphic of a current example of an offer**

We require 2 flyers to be re-designed which will include:
- Program Flyer
- Training calendar

Current flyers are attached - which are generally 2 pages long.

Program flyers
The newly designed flyer templates should cater for future use across multiple courses and have space for pictures that will be relevant to the content and also allow for additional content to be added if required (ie the template could be extended to a 3rd page)

Training Calendar
This flyer should be flexible to add additional courses as they arise and extend onto further pages easily.

Our branding guidelines and corporate colours should also be followed as attached.

We require editable files in photoshop/illustrator and PDF
The flyers should be A4 in size

Thank you for your time
Corinne

Target Market(s)

Students paying for services

Industry/Entity Type

Training

Font styles to use
Other font styles liked:
• As per brand guidelines

Requirements
Must have
• Corporate Brand Look and Feel

```html
<!DOCTYPE html>
<html lang="en">
<head>
<meta charset="utf-8">
<title>Training Program Flyer</title>
<link rel="stylesheet" href="https://fonts.googleapis.com/css2?family=Open+Sans:wght@400;600;700;800&display=swap">
<style>
  :root {
    --blue: #1b8fd8;
    --blue-deep: #146fb4;
    --navy: #0f3f73;
    --green: #8cc63f;
    --green-deep: #6fae2a;
    --orange: #e8561f;
    --yellow: #f6e34a;
    --ink: #4a4a4a;
    --white: #ffffff;
    --paper: #ffffff;
  }
  * { box-sizing: border-box; margin: 0; padding: 0; }
  html, body { width: 900px; height: 1200px; overflow: hidden; background: var(--paper); }
  body { font-family: "Open Sans", Arial, sans-serif; color: var(--ink); }

  .flyer { position: relative; width: 900px; height: 1200px; overflow: hidden; background: var(--paper); }

  .hero-photo {
    position: absolute; left: 0; top: 0; width: 900px; height: 560px;
    background: linear-gradient(120deg, #d7b48f 0%, #eed8bd 30%, #8fb7d8 60%, #4d7ea8 100%);
  }

  .bands { position: absolute; left: 0; top: 430px; width: 900px; height: 240px; }

  .offer {
    position: absolute; left: 28px; top: 468px; width: 270px; height: 130px;
    background: var(--white); transform: rotate(-6deg);
    box-shadow: 0 4px 10px rgba(0,0,0,.25);
    padding: 14px 16px;
  }
  .offer-amount { font-weight: 800; font-size: 30px; color: var(--blue); line-height: 1; }
  .offer-detail { font-size: 13px; color: var(--orange); font-weight: 700; margin-top: 6px; width: 150px; line-height: 1.25; }
  .offer-date {
    position: absolute; left: 16px; bottom: 12px; background: var(--blue); color: var(--white);
    font-weight: 800; font-size: 18px; padding: 2px 10px;
  }
  .offer-mascot {
    position: absolute; right: 12px; top: 12px; width: 84px; height: 70px; border-radius: 50%;
    background: linear-gradient(160deg, #6fc3f0, #1b8fd8);
  }

  .brand { position: absolute; right: 48px; top: 570px; text-align: right; }
  .brand-name { display: flex; align-items: center; gap: 12px; font-weight: 700; font-size: 44px; color: var(--navy); letter-spacing: -.5px; }
  .brand-dot { width: 26px; height: 26px; border-radius: 50%; background: var(--navy); }
  .brand-tag { font-size: 11px; font-weight: 600; letter-spacing: 1px; color: var(--navy); margin-top: 2px; }

  .titles { position: absolute; left: 0; top: 650px; width: 330px; height: 290px; background: var(--blue); }
  .titles-head {
    background: var(--navy); color: var(--white); font-weight: 800; font-size: 20px;
    line-height: 1.2; padding: 14px 22px; text-transform: uppercase;
  }
  .titles-list { list-style: none; padding: 14px 22px; }
  .titles-list li { color: var(--white); font-size: 16px; line-height: 1.55; position: relative; padding-left: 22px; }
  .titles-list li::before { content: ""; position: absolute; left: 0; top: 8px; width: 10px; height: 10px; background: var(--green); }

  .about { position: absolute; left: 330px; top: 660px; width: 570px; height: 280px; background: var(--green); padding: 26px 40px 0 40px; }
  .about-head { text-align: right; color: var(--white); font-weight: 800; font-size: 28px; letter-spacing: .5px; margin-bottom: 14px; }
  .about-text { color: var(--white); font-size: 16px; line-height: 1.5; }

  .rules { position: absolute; left: 0; top: 940px; width: 330px; height: 210px; background: var(--blue); padding: 20px 22px; }
  .rules-head { color: var(--white); font-weight: 800; font-size: 24px; line-height: 1.1; margin-bottom: 10px; }
  .rules-text { color: var(--yellow); font-weight: 700; font-size: 15px; line-height: 1.35; margin-bottom: 10px; }
  .rules-list { list-style: none; }
  .rules-list li { color: var(--white); font-size: 15px; line-height: 1.6; position: relative; padding-left: 20px; }
  .rules-list li::before { content: ""; position: absolute; left: 0; top: 8px; width: 9px; height: 9px; background: var(--green); }

  .entry { position: absolute; left: 330px; top: 940px; width: 570px; height: 210px; background: var(--white); padding: 22px 40px; }
  .entry-head { color: var(--orange); font-weight: 800; font-size: 24px; margin-bottom: 10px; }
  .entry-text { font-size: 14.5px; line-height: 1.5; color: var(--ink); }

  .foot { position: absolute; left: 0; top: 1150px; width: 900px; height: 50px; display: flex; }
  .foot-blue { width: 330px; background: var(--navy); }
  .foot-green { flex: 1; background: var(--green-deep); }
</style>
</head>
<body>
<main class="flyer">
  <div class="hero-photo" role="img" aria-label="Photo of smiling students working together at desks in a classroom"></div>

  <svg class="bands" viewBox="0 0 900 240" width="900" height="240" aria-hidden="true">
    <polygon points="0,120 900,20 900,230 0,230" fill="#1b8fd8"/>
    <polygon points="330,190 900,90 900,240 330,240" fill="#8cc63f"/>
    <polygon points="0,150 900,60 900,72 0,162" fill="#146fb4" opacity=".7"/>
    <rect x="0" y="220" width="330" height="20" fill="#1b8fd8"/>
  </svg>

  <aside class="offer">
    <div class="offer-amount">SAVE $100</div>
    <div class="offer-detail">Early Bird Special, book and pay before</div>
    <div class="offer-date">22nd December</div>
    <div class="offer-mascot" role="img" aria-label="Cartoon bird mascot illustration"></div>
  </aside>

  <div class="brand">
    <div class="brand-name"><span class="brand-dot"></span>Harbor Skills</div>
    <div class="brand-tag">EMPLOYMENT TRAINING &amp; RECRUITMENT</div>
  </div>

  <section class="titles">
    <h2 class="titles-head">Occupational titles<br>may include</h2>
    <ul class="titles-list">
      <li>Accommodation support worker</li>
      <li>Hostel supervisor</li>
      <li>Assistant hostel supervisor</li>
      <li>Personal care worker</li>
      <li>Care supervisor</li>
      <li>Care team leader</li>
      <li>Residential care worker</li>
    </ul>
  </section>

  <section class="about">
    <h2 class="about-head">ABOUT US</h2>
    <p class="about-text">Harbor Skills is a community based not for profit independent organisation that has been operating on the Northern Bay coast since 1977. The organisation exists to help people find and maintain employment.</p>
  </section>

  <section class="rules">
    <h2 class="rules-head">PACKAGING<br>RULES</h2>
    <p class="rules-text">15 units of competency are required for award of this qualification</p>
    <ul class="rules-list">
      <li>10 core units</li>
      <li>5 elective units</li>
    </ul>
  </section>

  <section class="entry">
    <h2 class="entry-head">ENTRY REQUIREMENTS</h2>
    <p class="entry-text">There are no formal entry requirements. However it is recommended that students have basic computer skills, good literacy, numeracy, communication and interpersonal skills. Applicants should have a caring and supportive attitude and be physically fit and able to lift heavy objects and be committed to the rights of elderly people.</p>
  </section>

  <div class="foot"><div class="foot-blue"></div><div class="foot-green"></div></div>
</main>
</body>
</html>
```